Wendlow Superfoods Packaging Design

We are looking for a design for our premium superfoods powders and blends. Packaging dimensions are 21cm x 13cm Kraft packaging (light brown background). This design should be a blueprint for other products that we will be marketing including lions mane mushroom, reishi mushroom, Chaga mushroom, Spirilina, bee pollen, açai powder and the like. The design should be clean but earthy, and the template replicable for other products.

```html
<!DOCTYPE html>
<html lang="en">
<head>
<meta charset="utf-8">
<title>Wendlow Superfoods – Lions Mane Mushroom Pack Front</title>
<link rel="stylesheet" href="https://fonts.googleapis.com/css2?family=Raleway:wght@600&family=Questrial&family=Jost:wght@600&display=swap">
<style>
  :root {
    --kraft: #c5996d;
    --leaf-green: #3e8b18;
    --ink: #111111;
    --paper: #ffffff;
    --shade-dark: #8e704f;
    --shade-light: #d8b898;
  }
  * { box-sizing: border-box; margin: 0; padding: 0; }
  html, body {
    width: 1200px;
    height: 900px;
    overflow: hidden;
    background: var(--paper);
  }
  .sheet {
    position: relative;
    width: 1200px;
    height: 900px;
    display: flex;
    justify-content: center;
    align-items: flex-start;
    gap: 31px;
    padding-top: 8px;
  }
  .pack {
    position: relative;
    width: 570px;
    height: 883px;
    background: var(--kraft);
    overflow: hidden;
  }
  .pack__backdrop {
    position: absolute;
    left: 286px;
    top: 494px;
    width: 284px;
    height: 389px;
    border-radius: 240px 0 0 0;
  }
  .pack--dark .pack__backdrop {
    background: linear-gradient(160deg, rgba(142,112,79,0.35) 0%, var(--shade-dark) 55%);
  }
  .pack--light .pack__backdrop {
    background: linear-gradient(160deg, rgba(216,184,152,0.35) 0%, var(--shade-light) 55%);
  }
  .brand-band {
    position: absolute;
    left: 85px;
    top: 188px;
    width: 400px;
    height: 189px;
    background: var(--leaf-green);
    border-radius: 0 58px 0 58px;
    display: flex;
    align-items: center;
    justify-content: center;
  }
  .brand-band__name {
    font-family: "Raleway", sans-serif;
    font-weight: 600;
    font-size: 30px;
    letter-spacing: 0.14em;
    line-height: 1.3;
    text-align: center;
  }
  .pack--dark .brand-band__name { color: var(--ink); }
  .pack--light .brand-band__name { color: var(--paper); }
  .tagline {
    position: absolute;
    left: 0;
    width: 100%;
    top: 470px;
    font-family: "Questrial", sans-serif;
    font-size: 24px;
    line-height: 29px;
    text-align: center;
    text-transform: uppercase;
    letter-spacing: 0.005em;
  }
  .pack--dark .tagline { color: var(--ink); }
  .pack--light .tagline { color: var(--paper); }
  .product-title {
    position: absolute;
    left: 84px;
    top: 600px;
    width: 402px;
    height: 140px;
  }
  .product-title__rule { fill: var(--leaf-green); }
  .product-title__sprig { fill: var(--leaf-green); }
  .product-title__name {
    font-family: "Jost", sans-serif;
    font-weight: 600;
    font-size: 35px;
    fill: var(--leaf-green);
  }
</style>
</head>
<body>
<main class="sheet">

  <section class="pack pack--dark">
    <div class="pack__backdrop" role="img" aria-label="Large faint leaf decoration in dark kraft tone"></div>
    <div class="brand-band">
      <p class="brand-band__name">WENDLOW<br>SUPERFOODS</p>
    </div>
    <p class="tagline">Premium superfoods<br>powders and blends</p>
    <svg class="product-title" viewBox="0 0 402 140" aria-labelledby="title-dark">
      <rect class="product-title__rule" x="0" y="18" width="160" height="4"/>
      <rect class="product-title__rule" x="242" y="18" width="160" height="4"/>
      <rect class="product-title__sprig" x="171" y="0" width="60" height="36" rx="14" role="img" aria-label="Small leaf sprig ornament"/>
      <text id="title-dark" class="product-title__name" x="0" y="82" textLength="402" lengthAdjust="spacingAndGlyphs">LIONS MANE MUSHROOM</text>
      <rect class="product-title__rule" x="0" y="113" width="160" height="4"/>
      <rect class="product-title__rule" x="242" y="113" width="160" height="4"/>
      <rect class="product-title__sprig" x="171" y="94" width="60" height="36" rx="14" role="img" aria-label="Small leaf sprig ornament"/>
    </svg>
  </section>

  <section class="pack pack--light">
    <div class="pack__backdrop" role="img" aria-label="Large faint leaf decoration in light kraft tone"></div>
    <div class="brand-band">
      <p class="brand-band__name">WENDLOW<br>SUPERFOODS</p>
    </div>
    <p class="tagline">Premium superfoods<br>powders and blends</p>
    <svg class="product-title" viewBox="0 0 402 140" aria-labelledby="title-light">
      <rect class="product-title__rule" x="0" y="18" width="160" height="4"/>
      <rect class="product-title__rule" x="242" y="18" width="160" height="4"/>
      <rect class="product-title__sprig" x="171" y="0" width="60" height="36" rx="14" role="img" aria-label="Small leaf sprig ornament"/>
      <text id="title-light" class="product-title__name" x="0" y="82" textLength="402" lengthAdjust="spacingAndGlyphs">LIONS MANE MUSHROOM</text>
      <rect class="product-title__rule" x="0" y="113" width="160" height="4"/>
      <rect class="product-title__rule" x="242" y="113" width="160" height="4"/>
      <rect class="product-title__sprig" x="171" y="94" width="60" height="36" rx="14" role="img" aria-label="Small leaf sprig ornament"/>
    </svg>
  </section>

</main>
</body>
</html>
```